Kovri DIGITAL HORIZON learning portal

We beed a flyer design to launch our new DIGITAL HORIZON Learning Portal. The flyer will be used in letter box drops and to give to small business to encourage sales of this new service.

ABOUT US:

We are a small training firm offering world class training solutions in the areas of:

1. Time Management
2. Sales skills
3. Strategic & High performance leadership
4. Sales Management
5. Personal Maximum Achievement.

You can find our website at www.kovri.com.au

ABOUT DIGITAL HORIZON Learning Portal:

We are launching an online learning portal called DIGITAL HORIZON Learning Portal which will allow anyone, anywhere in the world to take our courses online as long as they have access to a PC, smart phone and internet.

Taking an online course with Kovri through our DIGITAL HORIZON Learning Portal will allow students/participants to save over 50% of the normal price of attending a face to face training program.

There are over 80 different individual learning units that can be taken by a student/participant. The participant can choose to take any unit they wish building their own unique learning experience or they can take a full course in one of the subject areas listed above in the about us section.

ADVANTAGES OF USING THE Kovri DIGITAL HORIZON Learning Portal:

* Cost effective, save over 50% by learning online compared to attending a Kovri class room based programme.
* learning can be scheduled around work and family
* Reduces travel time and travel costs
* Students/participants have the option to select learning materials that meets their level of knowledge and interest.
* Complete flexibility to build a personalised learning experience.
* Students/participants can study anywhere they have access to a computer and Internet connection
* Self-paced learning modules allow students/participants to work at their own pace
* Develops knowledge of the Internet and computers skills that will help learners throughout their lives and careers
* Successfully completing online or computer-based courses builds self-knowledge and self-confidence and encourages students to take responsibility for their learning
* Join over 4 million people who have successfully undertaken the training world wide at a time & a place convenient to students/participants.
* pay securely using zentrapay
* learn based on a students/participants personal financial circumstances with individual units priced at $82.50 each (this is Australian dollars & includes GST)

The final design will be one that conveys flexibility of learning, cost effectiveness of the online learning solution. The flyer design can either be folded, single or double sided, A4 or A5 or DL size - whatever works best in the final outcome.

Industry/Entity Type

Small Business

Requirements
Must have
• The flyer must include:

* the "DIGITAL HORIZON Learning portal" logo and the "Kovri logo" and use the Kovri font. Several logos have been provided and the most appropriate ones can be chosen for the design. The font has been provided. (I do have other logo files in different file formats if required to aid designers)

* The flyer must direct people to the Kovri website www.kovri.com.au to pay, enrol and find out other information about the courses.

* The flyer must highlight cost effectiveness of the solution, the world wide popularity of the programs (over 4 million people have completed the programs world wide), flexibility of learning & the diversity of study areas.

Because of price changes in future of courses it would be very beneficial to be able to edit files in future to show new prices if and when that happens.

```html
<!DOCTYPE html>
<html lang="en">
<head>
<meta charset="utf-8">
<title>Kovri DIGITAL HORIZON Learning Portal</title>
<link href="https://fonts.googleapis.com/css2?family=Cabin+Sketch:wght@400;700&family=Open+Sans:ital,wght@0,400;0,700;1,400;1,700&display=swap" rel="stylesheet">
<style>
:root{
  --green:#5ee83a;
  --green-deep:#3fcf2a;
  --teal:#4ee6c8;
  --sky:#1fc3f0;
  --charcoal:#2a2a2a;
  --ink:#111;
  --white:#fff;
  --brand-teal:#1a9aa0;
  --link-blue:#3a6fd8;
  --rule:#777;
}
*{margin:0;padding:0;box-sizing:border-box}
html,body{width:811px;height:1200px;overflow:hidden;background:var(--white)}
body{position:relative;font-family:"Open Sans",sans-serif;color:var(--ink)}
.abs{position:absolute}

/* panels */
.stripes-dark{background:repeating-linear-gradient(120deg,#2b2b2b 0 28px,#353535 28px 56px)}
.panel-about{left:0;top:0;width:300px;height:600px}
.panel-about .green{left:65px;top:0;width:235px;height:600px;background:repeating-linear-gradient(120deg,var(--green) 0 40px,#66ec44 40px 80px)}
.panel-contact{left:300px;top:0;width:235px;height:600px;background:var(--white)}
.panel-cover{left:535px;top:0;width:276px;height:600px;background:linear-gradient(90deg,#fff 0,#d6eef6 30px,var(--sky) 30px)}
.panel-services{left:0;top:600px;width:300px;height:600px}
.panel-services .teal{left:0;top:0;width:65px;height:600px;background:linear-gradient(90deg,var(--teal),#7ef3da)}
.panel-portal{left:300px;top:600px;width:235px;height:600px;background:var(--white)}
.panel-benefits{left:535px;top:600px;width:276px;height:600px;background:var(--white)}
.panel-benefits .strip{left:210px;top:0;width:66px;height:600px;background:linear-gradient(90deg,#fff,var(--green))}
.fold{width:1px;background:var(--rule);opacity:.6}

/* headings */
.pill{display:flex;align-items:center;gap:14px;height:56px;border-radius:10px;background:var(--white);border-left:5px solid var(--ink);padding-left:12px;box-shadow:0 1px 4px rgba(0,0,0,.25)}
.pill h2{font-family:"Cabin Sketch",sans-serif;font-weight:400;font-size:20px;letter-spacing:.5px;color:var(--ink)}
.pill.sky{background:var(--sky)}
.pill.lime{background:var(--green)}
.tick{width:22px;height:22px;flex:none}

.about-text{left:18px;top:88px;width:262px;font-size:7.6px;line-height:15.7px;font-weight:700;font-style:italic;color:var(--white);text-shadow:0 0 1px rgba(0,0,0,.3)}
.about-text p+p{margin-top:15.7px}

.contact-title{left:305px;top:38px;width:190px;border-top:3px double #999;border-bottom:none;padding-top:14px;font-family:"Cabin Sketch",sans-serif;font-size:22px;color:var(--ink)}
.contact-rule{left:305px;width:190px;height:3px;border-top:3px double #999}
.contact-row{left:283px;display:flex;gap:10px;font-size:10px;line-height:19px;color:var(--link-blue);text-shadow:0 0 4px rgba(58,111,216,.5)}
.contact-row .ico{width:17px;height:17px;background:var(--ink);display:flex;align-items:center;justify-content:center;margin-top:1px;flex:none}
.contact-row b{font-weight:700}

.brand-mark{display:flex;flex-direction:column;align-items:center}
.brand-square{background:var(--brand-teal)}
.brand-name{font-family:"Open Sans",sans-serif;font-weight:400;color:#333}
.site{font-family:"Open Sans",sans-serif;font-weight:700;font-size:12px;color:var(--ink);letter-spacing:.5px}

.portal-badge{left:612px;top:55px;width:148px;height:30px;background:#222;color:#f0c419;font-weight:700;font-size:13px;display:flex;align-items:center;justify-content:center;letter-spacing:.5px}

.photo{border:0}

.services-list{left:48px;top:703px;width:220px;font-style:italic;font-size:14.5px;line-height:20px;color:var(--white);padding-left:20px}
.services-list li::marker{color:var(--white)}

.portal-text{left:305px;top:697px;width:228px;font-size:9.4px;line-height:16.3px;font-weight:700;font-style:italic;color:var(--ink)}
.portal-text p+p{margin-top:16.3px}

.benefits-text{left:548px;top:686px;width:225px;font-size:11px;line-height:13.55px;color:var(--ink)}
.benefits-text em{font-weight:700}
</style>
</head>
<body>

<!-- top row -->
<section class="abs panel-about stripes-dark">
  <div class="abs green"></div>
</section>
<section class="abs panel-contact"></section>
<section class="abs panel-cover"></section>

<!-- bottom row -->
<section class="abs panel-services stripes-dark">
  <div class="abs teal"></div>
</section>
<section class="abs panel-portal"></section>
<section class="abs panel-benefits">
  <div class="abs strip"></div>
</section>

<div class="abs fold" style="left:270px;top:10px;height:580px"></div>
<div class="abs fold" style="left:535px;top:10px;height:580px"></div>
<div class="abs fold" style="left:270px;top:610px;height:580px"></div>
<div class="abs fold" style="left:535px;top:610px;height:580px"></div>
<div class="abs" style="left:0;top:599px;width:811px;height:2px;background:#ddd"></div>

<!-- About us -->
<header class="abs pill" style="left:70px;top:20px;width:182px">
  <h2>ABOUT US</h2>
  <svg class="tick" viewBox="0 0 22 22"><path d="M2 2h18v14H9l-5 4v-4H2z" fill="var(--green-deep)"/><path d="M5 9l4 4 9-10" stroke="#111" stroke-width="3" fill="none"/></svg>
</header>
<div class="abs about-text">
  <p>MARCUS DELVANE specialises in working with leaders and sales teams who want to achieve their goals quickly. With over 20 years of experience in sales management, leadership, strategy development and business-solution selling in sales and service fields, particularly the health insurance industry, Marcus has the expertise and dedication to ensure that his clients achieve rapid results and sustained outcomes. Based in Sydney, Marcus has a strong record of success in efficiently managing multimillion-dollar portfolios, perfecting highly-motivated national sales teams, and consistently over-achieving sales and profit margin targets in competitive market conditions. His tertiary qualifications include a Bachelor of Marketing from Northfield State University, and both a Master in Financial Management and an MBA from Harbourside Graduate School of Management.</p>
  <p>TREVOR ASHCOMBE is an accomplished senior leader with over 20 years of experience in sales and service fields including insurance, business, retail, and government. His academic qualifications comprise a Bachelor of Business (Marketing) and a Graduate Certificate of Retail Management. Trevor has a proven track record of exceeding revenue and margin targets through his dynamic leadership of teams in multi-site businesses. His success in the corporate sector and the consistent feedback he received from colleagues and customers who found his input inspirational and transformative, lead Trevor to start his company Kovri with the aim of empowering organisations and teams to reach their goals of increased revenues and reduced costs.</p>
</div>

<!-- Contact -->
<h2 class="abs contact-title">CONTACT US</h2>
<div class="abs contact-row" style="top:108px">
  <span class="ico"><svg width="11" height="11" viewBox="0 0 11 11"><path d="M5.5 1L1 5h1.5v5h2.5V7h1v3h2.5V5H10z" fill="#fff"/></svg></span>
  <span>4/27 Harlow Street Brenton, NSW 2048<br><b>www.kovri.com.au</b></span>
</div>
<div class="abs contact-row" style="top:157px">
  <span class="ico"><svg width="11" height="11" viewBox="0 0 11 11"><path d="M2 1h2l1 3-1.3 1a6 6 0 0 0 2.3 2.3L7 6l3 1v2c0 .6-.4 1-1 1A8 8 0 0 1 1 2c0-.6.4-1 1-1z" fill="#fff"/></svg></span>
  <span>+61 2 5550 174</span>
</div>
<div class="abs contact-row" style="top:211px">
  <span class="ico"><svg width="11" height="11" viewBox="0 0 11 11"><rect x="1" y="2.5" width="9" height="6.5" fill="#fff"/><path d="M1 2.5l4.5 4 4.5-4" stroke="#111" fill="none"/></svg></span>
  <span>trevor.ashcombe@kovri.com.au<br>marcus.delvane@kovri.com.au</span>
</div>
<div class="abs contact-rule" style="top:262px"></div>

<div class="abs brand-mark" style="left:310px;top:280px;width:215px">
  <div class="brand-square" style="width:130px;height:155px"></div>
  <div class="brand-name" style="font-size:64px;line-height:1.2;margin-top:6px">Kovri</div>
</div>
<div class="abs site" style="left:347px;top:563px">www.kovri.com.au</div>

<!-- Cover -->
<div class="abs portal-badge">DIGITAL HORIZON</div>
<div class="abs photo" role="img" aria-label="Photo of a businesswoman holding a tablet and stylus against a blue digital background" style="left:580px;top:118px;width:231px;height:327px;background:linear-gradient(135deg,#1a5fb4 0%,#3d8ce0 45%,#8d8f96 70%,#2f3238 100%)"></div>
<div class="abs brand-mark" style="left:640px;top:452px;width:85px">
  <div class="brand-square" style="width:70px;height:70px"></div>
  <div class="brand-name" style="font-size:20px;color:#fff;line-height:1.3">Kovri</div>
</div>
<div class="abs site" style="left:620px;top:563px">www.kovri.com.au</div>

<!-- Services -->
<header class="abs pill" style="left:45px;top:622px;width:183px">
  <h2>SERVICES</h2>
  <svg class="tick" viewBox="0 0 22 22"><path d="M2 2h18v14H9l-5 4v-4H2z" fill="var(--green-deep)"/><path d="M5 9l4 4 9-10" stroke="#111" stroke-width="3" fill="none"/></svg>
</header>
<ol class="abs services-list">
  <li>Time Management</li>
  <li>Sales skills</li>
  <li>Strategic &amp; High performance leadership</li>
  <li>Sales Management</li>
  <li>Personal Maximum Achievement.</li>
</ol>
<div class="abs photo" role="img" aria-label="Photo of a business team gathered around a laptop" style="left:20px;top:903px;width:232px;height:147px;background:linear-gradient(120deg,#e9eef2 0%,#6a7480 45%,#2d3440 75%,#dfe5ea 100%)"></div>

<!-- Portal -->
<header class="abs pill sky" style="left:322px;top:620px;width:183px">
  <h2 style="font-size:14px;line-height:1.05;text-align:center">DIGITAL HORIZON<br>Learning Portal</h2>
  <svg class="tick" viewBox="0 0 22 22"><path d="M2 2h18v14H9l-5 4v-4H2z" fill="var(--green-deep)"/><path d="M5 9l4 4 9-10" stroke="#111" stroke-width="3" fill="none"/></svg>
</header>
<div class="abs portal-text">
  <p>We are launching an online learning portal called DIGITAL HORIZON Learning Portal which will allow anyone, anywhere in the world to take our courses online as long as they have access to a PC, smart phone and internet.</p>
  <p>Taking an online course with Kovri through our DIGITAL HORIZON Learning Portal will allow students/participants to save over 50% of the normal price of attending a face to face training program.</p>
  <p>There are over 80 different individual learning units that can be taken by a student/participant. The participant can choose to take any unit they wish building their own unique learning experience or they can take a full course in one of the subject areas listed above in the about us section.</p>
</div>
<div class="abs photo" role="img" aria-label="Photo of a computer keyboard with a red online learning key" style="left:305px;top:1023px;width:225px;height:150px;background:linear-gradient(160deg,#6b6f75 0%,#2a2c30 55%,#b02020 62%,#2a2c30 70%,#111 100%)"></div>

<!-- Benefits -->
<header class="abs pill lime" style="left:568px;top:620px;width:183px">
  <h2>BENEFITS</h2>
  <svg class="tick" viewBox="0 0 22 22"><path d="M2 2h18v14H9l-5 4v-4H2z" fill="var(--green-deep)"/><path d="M5 9l4 4 9-10" stroke="#111" stroke-width="3" fill="none"/></svg>
</header>
<div class="abs benefits-text">
  * <em>Cost effective</em>, save over 50% by learning online compared to attending a Kovri class room based programme.<br>
  * <em>learning</em> can be scheduled around work and family<br>
  * <em>Reduces</em> travel time and travel costs<br>
  * <em>Students/participants</em> have the option to select learning materials that meets their level of knowledge and interest.<br>
  * <em>Complete flexibility</em> to build a personalised learning experience.<br>
  * <em>Students/participants</em> can study anywhere they have access to a computer and Internet connection<br>
  * <em>Self-paced</em> learning modules allow students/ participants to work at their own pace<br>
  * <em>Develops knowledge</em> of the Internet and computers skills that will help learners throughout their lives and careers<br>
  * <em>Successfully</em> completing online or computer-based courses builds self-knowledge and self-confidence and encourages students to take responsibility for their learning<br>
  * <em>Join over 4 million people</em> who have successfully undertaken the training world wide at a time &amp; a place convenient to students/participants.<br>
  * <em>pay securely using zentrapay</em><br>
  * <em>learn based</em> on a students/participants personal financial circumstances with individual units priced at $82.50 each (this is Australian dollars &amp; includes GST)
</div>

</body>
</html>
```